- Redesign our business card
- Logo remains unchanged
- Current business card attached

Target Market(s)

We are a property management company

Industry/Entity Type

Business

```html
<!DOCTYPE html>
<html lang="en">
<head>
<meta charset="utf-8">
<title>Ashford Property Group – Business Card</title>
<link href="https://fonts.googleapis.com/css2?family=Exo+2:wght@400;700&display=swap" rel="stylesheet">
<style>
  :root {
    --olive: #857f43;
    --olive-text: #7d7a3c;
    --slate: #6d6e71;
    --ink: #231f20;
    --paper: #ffffff;
    --edge: #8a8a8a;
  }
  * { box-sizing: border-box; margin: 0; padding: 0; }
  html, body {
    width: 886px; height: 1200px; overflow: hidden;
    background: var(--paper);
    font-family: "Exo 2", sans-serif;
  }
  .sheet { position: relative; width: 886px; height: 1200px; }

  .card {
    position: absolute; left: 43px; width: 787px; height: 450px;
    border-radius: 26px; overflow: hidden;
    border: 1px solid var(--edge);
    box-shadow: 4px 5px 6px rgba(0,0,0,0.35);
    background: var(--paper);
  }
  .card--front { top: 50px; }
  .card--back {
    top: 559px;
    background: radial-gradient(ellipse 430px 330px at 387px 195px,
      #ffffff 0%, #f4f3ea 22%, #c9c59f 52%, var(--olive) 88%);
  }
  .card__band {
    position: absolute; left: 0; right: 0; top: 397px; bottom: 0;
    background: var(--slate); color: #fff;
    display: flex; align-items: center;
    font-size: 21px; white-space: nowrap;
  }

  .holder { position: absolute; left: 43px; top: 80px; }
  .holder__name {
    color: var(--olive-text); font-weight: 700; font-size: 31px;
    letter-spacing: 0.6px; line-height: 1;
  }
  .holder__title { color: var(--ink); font-size: 24px; margin-top: 6px; }

  .address {
    position: absolute; left: 43px; top: 279px;
    font-style: normal;
    font-size: 18px; line-height: 25px; color: var(--ink);
    text-transform: uppercase; letter-spacing: 0.3px;
  }
  .contacts {
    position: absolute; left: 472px; top: 279px;
    list-style: none; font-size: 18px; line-height: 25px; color: var(--ink);
  }
  .contacts li { display: flex; align-items: center; height: 25px; }
  .contacts svg { width: 22px; height: 18px; margin-right: 9px; fill: var(--olive); }

  .services { padding-left: 43px; }
  .services .sep { margin: 0 10px; }

  .brand {
    position: absolute; left: 0; right: 0; top: 278px;
    display: flex; justify-content: center; align-items: center; gap: 12px;
  }
  .brand__mark { width: 22px; height: 22px; background: var(--olive); }
  .brand__name {
    font-weight: 700; font-size: 29px; letter-spacing: 1px;
    color: var(--slate); text-transform: uppercase;
  }
  .web { justify-content: center; font-size: 23px; }
</style>
</head>
<body>
<main class="sheet">

  <section class="card card--front" aria-label="Card front">
    <div class="holder">
      <h1 class="holder__name">DANIEL HARCOURT</h1>
      <p class="holder__title">Licensed Strata Manager</p>
    </div>

    <address class="address">
      PO Box 418,<br>
      Redfern Heights NSW 2016<br>
      12/40-46 Marlow Lane<br>
      Ashfield Park NSW 2131
    </address>

    <ul class="contacts">
      <li>
        <svg viewBox="0 0 22 18" aria-label="Phone"><path d="M1 6c0-3 4-4 10-4s10 1 10 4v1h-5V5H6v2H1z"/><rect x="4" y="8" width="14" height="9" rx="1"/></svg>
        02 9555 0147
      </li>
      <li>
        <svg viewBox="0 0 22 18" aria-label="Fax"><rect x="6" y="1" width="10" height="6" fill="none" stroke="#857f43" stroke-width="1.5"/><rect x="2" y="7" width="18" height="10" rx="1"/><rect x="5" y="10" width="12" height="1.5" fill="#fff"/><rect x="5" y="13" width="12" height="1.5" fill="#fff"/></svg>
        02 9555 0293
      </li>
      <li>
        <svg viewBox="0 0 22 18" aria-label="Mobile"><g transform="rotate(35 11 9)"><rect x="7" y="0" width="8" height="18" rx="1.5"/><rect x="8.5" y="2" width="5" height="4" fill="#fff"/></g></svg>
        0412 000 384
      </li>
      <li>
        <svg viewBox="0 0 22 18" aria-label="Email"><rect x="2" y="3" width="18" height="12" fill="none" stroke="#857f43" stroke-width="1.5"/><path d="M2 3l9 7 9-7" fill="none" stroke="#857f43" stroke-width="1.5"/></svg>
        info@ashfordproperty.com.au
      </li>
    </ul>

    <div class="card__band services">
      <span class="services__line">Strata Management<span class="sep">|</span>Community Management<span class="sep">|</span>Property Management</span>
    </div>
  </section>

  <section class="card card--back" aria-label="Card back">
    <div class="brand">
      <span class="brand__mark"></span>
      <span class="brand__name">Ashford Property Group</span>
    </div>
    <div class="card__band web">www.ashfordproperty.com.au</div>
  </section>

</main>
</body>
</html>
```